Business cards for Norwegian software consultancy business

We are in need of business cards for our Norwegian consultancy company.
“Talvik Brensor AS” specializes in software development, architecture and agile methodology, providing mostly on-site services at customers.
The cards should reflect a certain level of business professionalism with an elegant touch, while paying tribute to our modern and technological heritage. Our logo should be featured, as well as room for basic information about the cardholder and legal information of the company (company name, address and VAT number).
We would like our cards to reflect that we are a modern consulting company. It should present a professional image that people will remember. The texture and color pallette should reflect our professionalism and reliability, so we prefer a light color pallette with colors such as gray, white, blue and black. The number of colors used should however not be overwhelming, with the text being distinct and readable.
We are open to untraditional layouts and playful designs as long as they communicate the intent stated above.
You could also take a look at our website http://www.brensor.no for input on our visual profile.
Our logo is attached in the form of vectors and rasterized PNG. Please comment if you would like the black-white and/or inverted versions as well.
Architecture
Company information:
Talvik Brensor AS
Lindeholtveien 7, 3142 Vestskogen
461 82 915
info@brensor.no
www.brensor.no
Employee information:
Full name
Title
Email
Phone

```html
<!DOCTYPE html>
<html lang="en">
<head>
<meta charset="utf-8">
<title>Talvik Brensor AS – Business Card Options</title>
<link rel="stylesheet" href="https://fonts.googleapis.com/css2?family=Oswald:wght@400;500&family=Open+Sans:wght@400&display=swap">
<style>
  :root {
    --sheet-bg: #ffffff;
    --ink: #161616;
    --ink-soft: #2a2a2a;
    --caption: #333333;
    --band-grey: #d3d3d3;
    --card-light: #ededed;
    --pattern-top: #e6e6e6;
    --pattern-bottom: #f1f1f1;
    --accent-blue: #4a8fcb;
    --shadow: rgba(0, 0, 0, 0.28);
  }

  * { box-sizing: border-box; margin: 0; padding: 0; }

  html, body {
    width: 847px;
    height: 1200px;
    overflow: hidden;
    background: var(--sheet-bg);
  }

  .sheet {
    position: relative;
    width: 847px;
    height: 1200px;
  }

  .sheet-title {
    position: absolute;
    top: 26px;
    left: 0;
    width: 100%;
    text-align: center;
    font-family: "Open Sans", sans-serif;
    font-size: 31px;
    font-weight: 400;
    color: var(--ink);
  }

  .option-caption {
    position: absolute;
    width: 100%;
    left: 0;
    text-align: center;
    font-family: "Open Sans", sans-serif;
    font-size: 15px;
    color: var(--caption);
  }
  .caption-one { top: 664px; }
  .caption-two { top: 1084px; }

  .card {
    position: absolute;
    overflow: hidden;
    background: var(--card-light);
    box-shadow: 3px 4px 7px var(--shadow);
  }

  .card-portrait {
    left: 269px;
    top: 92px;
    width: 334px;
    height: 550px;
  }

  .card-landscape {
    left: 148px;
    top: 729px;
    width: 550px;
    height: 332px;
  }

  .card-texture {
    position: absolute;
    inset: 0;
    background: linear-gradient(160deg, var(--pattern-top), var(--pattern-bottom));
  }

  .top-band {
    position: absolute;
    inset: 0;
    background: var(--band-grey);
    clip-path: polygon(0 0, 100% 0, 100% 223px, 0 319px);
  }

  .holder {
    position: absolute;
    padding-left: 24px;
    font-family: "Oswald", sans-serif;
    color: var(--ink);
  }
  .holder::before {
    content: "";
    position: absolute;
    left: 0;
    top: 0;
    width: 11px;
    height: 100%;
    background: var(--ink);
  }

  .card-portrait .holder { left: 16px; top: 53px; height: 155px; }
  .card-landscape .holder { left: 23px; top: 82px; height: 161px; }

  .holder-name {
    font-size: 33px;
    font-weight: 500;
    line-height: 1;
    margin-top: -2px;
    letter-spacing: 0.2px;
  }
  .holder-title {
    font-size: 21px;
    font-weight: 400;
    line-height: 1.25;
    margin-top: 3px;
  }
  .holder-contact {
    list-style: none;
    margin-top: 19px;
    font-size: 16.5px;
    font-weight: 400;
    line-height: 1.55;
    color: var(--ink-soft);
  }

  .brand {
    position: absolute;
    display: flex;
    align-items: center;
    gap: 12px;
    font-family: "Oswald", sans-serif;
    font-weight: 400;
    color: var(--ink);
    letter-spacing: 1px;
    line-height: 1;
  }
  .brand-square {
    width: 16px;
    height: 16px;
    background: var(--accent-blue);
    flex: none;
  }

  .card-portrait .brand {
    left: 14px;
    top: 462px;
    font-size: 36px;
  }

  .card-landscape .brand {
    right: 22px;
    top: 12px;
    bottom: 14px;
    flex-direction: column-reverse;
    font-size: 34px;
  }
  .card-landscape .brand-name {
    writing-mode: vertical-rl;
    transform: rotate(180deg);
  }
</style>
</head>
<body>
  <main class="sheet">
    <h1 class="sheet-title">Design mock-ups</h1>

    <section class="card card-portrait" aria-label="Business card, portrait option">
      <div class="card-texture" role="img" aria-label="Faint light grey repeating brand-shape texture"></div>
      <div class="top-band"></div>
      <div class="holder">
        <p class="holder-name">Henrik Solvang</p>
        <p class="holder-title">CEO, Talvik Brensor AS</p>
        <ul class="holder-contact">
          <li>info@brensor.no</li>
          <li>Lindeholtveien 7 -3142 Vestskogen</li>
          <li>461 82 915</li>
        </ul>
      </div>
      <div class="brand">
        <span class="brand-square"></span>
        <span class="brand-name">TALVIK BRENSOR</span>
      </div>
    </section>
    <p class="option-caption caption-one">Option-1</p>

    <section class="card card-landscape" aria-label="Business card, landscape option">
      <div class="card-texture" role="img" aria-label="Faint light grey repeating brand-shape texture"></div>
      <div class="holder">
        <p class="holder-name">Henrik Solvang</p>
        <p class="holder-title">CEO, Talvik Brensor AS</p>
        <ul class="holder-contact">
          <li>info@brensor.no</li>
          <li>Lindeholtveien 7 -3142 Vestskogen</li>
          <li>461 82 915</li>
        </ul>
      </div>
      <div class="brand">
        <span class="brand-square"></span>
        <span class="brand-name">TALVIK BRENSOR</span>
      </div>
    </section>
    <p class="option-caption caption-two">Option-2</p>
  </main>
</body>
</html>
```